Envelope Design Project

I will need two envelopes to be designed:-

DL size
C4 size

Please see uploaded documents for Design specs:

1) Design specs provided by printer (doc called DL Envelope Specs)
2) Design specs to comply with Kestrel Mailways requirements (doc called Kestrel Mailways Envelope Design Requirements)

Please adhere to the above for final design. Many thanks.

Target Market(s)

Real Estate Agents, Strata Managers, Builders, Architects, Business Owners

Industry/Entity Type

Printer

Requirements
Must have
• In top left corner
- Logo
- Return address - Suite 5, 19 Wattlebark Rd, Marrowick, NSW 2417

```html
<!DOCTYPE html>
<html lang="en">
<head>
<meta charset="utf-8">
<title>Corvane Asbestos &amp; Safety — C4 Envelope</title>
<link href="https://fonts.googleapis.com/css2?family=Jost:wght@400;500&display=swap" rel="stylesheet">
<style>
  :root {
    --backdrop: #e9e9e9;
    --paper: #ffffff;
    --paper-edge: #dcdcdc;
    --brand-navy: #243156;
    --brand-green: #8bbd3f;
    --ink: #222222;
  }
  html, body {
    margin: 0;
    padding: 0;
    width: 1200px;
    height: 900px;
    overflow: hidden;
    background: var(--backdrop);
  }
  .canvas {
    position: relative;
    width: 1200px;
    height: 900px;
  }
  .envelope-shape {
    position: absolute;
    inset: 0;
  }
  .envelope-shape .body { fill: var(--paper); }
  .envelope-shape .flap { fill: var(--paper); stroke: var(--paper-edge); stroke-width: 1; }
  .envelope-shape .fold { stroke: var(--paper-edge); stroke-width: 1; }
  .envelope-shape .band-navy { fill: var(--brand-navy); }
  .envelope-shape .band-green { fill: var(--brand-green); }

  .sender {
    position: absolute;
    left: 153px;
    top: 214px;
    font-family: "Jost", sans-serif;
    color: var(--brand-navy);
  }
  .brand-name {
    margin: 0;
    font-size: 44px;
    font-weight: 500;
    line-height: 48px;
    letter-spacing: 0.2px;
  }
  .brand-tagline {
    margin: 6px 0 0 1px;
    font-size: 18px;
    font-weight: 500;
    line-height: 20px;
    letter-spacing: 0.3px;
  }
  .return-address {
    margin: 12px 0 0 1px;
    font-style: normal;
    font-size: 13px;
    line-height: 16px;
    color: var(--ink);
  }
</style>
</head>
<body>
<main class="canvas">
  <svg class="envelope-shape" width="1200" height="900" viewBox="0 0 1200 900" aria-hidden="true">
    <path class="flap" d="M989 131 L1072 140 Q1088 142 1090 160 L1115 450 L1090 710 Q1088 728 1070 731 L989 769 Z"/>
    <rect class="body" x="85" y="131" width="904" height="638"/>
    <line class="fold" x1="989" y1="131" x2="989" y2="769"/>
    <polygon class="band-navy" points="85,740 412,740 397,769 85,769"/>
    <polygon class="band-green" points="422,728 989,728 989,769 401,769"/>
  </svg>

  <header class="sender">
    <h1 class="brand-name">Corvane</h1>
    <p class="brand-tagline">ASBESTOS &amp; SAFETY</p>
    <address class="return-address">
      Suite 5, 19 Wattlebark Rd<br>
      Marrowick, NSW 2417
    </address>
  </header>
</main>
</body>
</html>
```